DominicRaleigh

I will be video blogging 1 - 5 minute instructional videos about all kind or stuff

I want it took look clean.
I have secured Dominicraleigh.com
Do you design youtube pages as well.
I will upload to youtube and correspond with websites.
Website wil include
videos with longer written description
how to book me.
where I am speaking at next
Thank you

Reason: my design is going to be more detailed than i had expected

Reason: still have changes

Youtube

```html
<!DOCTYPE html>
<html lang="en">
<head>
<meta charset="utf-8">
<title>dominicraleigh.com</title>
<link href="https://fonts.googleapis.com/css2?family=Source+Sans+3:wght@300;400;600;700&display=swap" rel="stylesheet">
<style>
:root{
  --bg-dark:#3b1c03;
  --bg-mid:#5a2f06;
  --blue:#00aeef;
  --blue-deep:#0a9ad6;
  --blue-light:#2bbdf3;
  --white:#ffffff;
  --panel:#f0f0f0;
  --text:#5a5a5a;
  --heading:#1a1a1a;
  --red:#e01b1b;
  --video:#0d0d0d;
  --rule:#e2e2e2;
}
*{box-sizing:border-box;margin:0;padding:0}
html,body{width:1200px;height:1000px;overflow:hidden}
body{
  position:relative;
  font-family:"Source Sans 3",Arial,sans-serif;
  background:radial-gradient(ellipse at 50% 35%,var(--bg-mid) 0%,#4a2504 55%,var(--bg-dark) 100%);
}
.site-name{
  position:absolute;left:134px;top:30px;
  font-size:40px;font-weight:700;color:var(--white);letter-spacing:-0.5px;line-height:46px;
}
.hero-photo{
  position:absolute;left:121px;top:94px;width:610px;height:229px;
  background:linear-gradient(90deg,#b9b25e 0%,#d8d29a 35%,#eee6cf 60%,#e9dcc4 100%);
}
.featured{position:absolute;left:731px;top:94px;width:350px;height:229px;background:var(--video)}
.featured-title{
  height:34px;background:var(--blue);color:var(--white);
  font-size:16px;font-weight:600;text-align:center;line-height:34px;
}
.featured-screen{position:relative;height:195px;background:linear-gradient(180deg,#1b1b1b,#0b0b0b)}
.play{
  position:absolute;display:flex;align-items:center;gap:10px;color:var(--white);font-weight:400;
}
.play svg{display:block}
.featured .play{left:81px;top:56px;font-size:26px}
.progress{position:absolute;left:0;right:0;height:3px;background:#444}
.progress span{display:block;height:100%;background:#c8141b}
.featured .progress{top:196px}
.nav{
  position:absolute;left:121px;top:323px;width:960px;height:53px;
  background:linear-gradient(180deg,#12bdf6,var(--blue-deep));
}
.nav-links{position:absolute;left:13px;top:0;display:flex;gap:18px;list-style:none}
.nav-links li{color:var(--white);font-size:16px;font-weight:600;line-height:53px}
.nav-pointer{position:absolute;left:12px;top:53px;width:0;height:0;border-left:7px solid transparent;border-right:7px solid transparent;border-top:11px solid var(--blue-deep)}
.search{
  position:absolute;left:665px;top:10px;width:206px;height:34px;background:var(--white);
  border:1px solid #333;border-radius:4px;
}
.search span{position:absolute;left:11px;top:7px;font-size:14px;color:#9a9a9a}
.search .divider{position:absolute;left:164px;top:5px;width:1px;height:22px;background:#888}
.search svg{position:absolute;left:172px;top:6px}
.social{position:absolute;left:882px;top:9px;list-style:none}
.social li{display:flex;align-items:center;gap:5px;color:var(--white);font-size:12px;font-weight:600;line-height:17px}
.social li::before{content:"";width:9px;height:9px;border-radius:50%;background:var(--white)}
.content{position:absolute;left:121px;top:376px;width:960px;height:624px;background:var(--white)}
.post-title{position:absolute;left:12px;top:20px;font-size:29px;font-weight:400;color:var(--heading)}
.post-date{position:absolute;left:12px;top:56px;font-size:16px;color:#888}
.post-date time{color:var(--red)}
.post-video{
  position:absolute;left:13px;top:94px;width:567px;height:354px;
  border:6px solid var(--blue);border-radius:6px;background:var(--video);
}
.post-video .screen{position:absolute;inset:0 0 30px 0;background:linear-gradient(160deg,#2a2a22,#121210 60%,#0a0a0a)}
.post-video .play{left:184px;top:150px;font-size:24px}
.post-video .progress{bottom:30px}
.controls{position:absolute;left:0;right:0;bottom:0;height:30px;background:#111;color:#bbb;font-size:10px;display:flex;align-items:center;gap:14px;padding-left:16px}
.post-excerpt{position:absolute;left:15px;top:456px;width:565px;font-size:15.6px;line-height:18px;color:var(--text);font-weight:400}
.btn{
  position:absolute;background:var(--blue);color:var(--white);text-align:center;border-radius:4px;
}
.read-more{left:13px;top:556px;width:155px;height:38px;line-height:38px;font-size:17px}
.post-rule{position:absolute;left:13px;top:616px;width:550px;height:2px;background:var(--rule)}
.widget{position:absolute;left:672px;width:272px;background:var(--panel);border:1px solid var(--blue);border-radius:6px;overflow:hidden}
.widget-title{height:38px;background:var(--blue);color:var(--white);font-size:16px;font-weight:600;text-align:center;line-height:38px}
.recent{top:28px;height:356px}
.recent-list{list-style:none;position:absolute;left:11px;top:55px}
.recent-list li{position:relative;height:87px}
.thumb{position:absolute;left:0;top:0;width:126px;height:74px;border:2px solid var(--blue);background:linear-gradient(135deg,#3a4a5a,#1a1a1a)}
.thumb .play{left:18px;top:22px;font-size:11px;gap:5px}
.thumb .duration{position:absolute;right:4px;bottom:2px;color:var(--white);font-size:10px;font-weight:600}
.recent-list h3{position:absolute;left:140px;top:4px;width:110px;font-size:15px;font-weight:400;line-height:17px;color:var(--heading)}
.see-more{left:67px;top:319px;width:132px;height:24px;line-height:24px;font-size:14px;font-weight:600}
.hatch{position:absolute;left:674px;top:410px;width:264px;height:8px;background:repeating-linear-gradient(135deg,#bdbdbd 0 2px,#e8e8e8 2px 4px)}
.archives{top:440px;height:200px}
</style>
</head>
<body>
<header>
  <div class="site-name">dominicraleigh.com</div>
  <div class="hero-photo" role="img" aria-label="Portrait of Dominic Raleigh over a word cloud about instruction and feedback"></div>
  <section class="featured">
    <h2 class="featured-title">FEATURED VIDEO</h2>
    <div class="featured-screen">
      <div class="play">
        <svg width="48" height="48" viewBox="0 0 48 48"><circle cx="24" cy="24" r="21" fill="none" stroke="#fff" stroke-width="4"/><path d="M19 14v20l16-10z" fill="#fff"/></svg>
        PLAY NOW!
      </div>
      <div class="progress"><span style="width:96%"></span></div>
    </div>
  </section>
  <nav class="nav">
    <ul class="nav-links"><li>Home</li><li>Videos</li><li>Discussion</li><li>About</li></ul>
    <div class="nav-pointer"></div>
    <div class="search">
      <span>search</span><div class="divider"></div>
      <svg width="22" height="22" viewBox="0 0 22 22"><circle cx="8" cy="8" r="6" fill="none" stroke="#333" stroke-width="2.4"/><path d="M12.5 12.5l7 7" stroke="#333" stroke-width="3" stroke-linecap="round"/></svg>
    </div>
    <ul class="social"><li>Folio</li><li>Chirpr</li></ul>
  </nav>
</header>
<main class="content">
  <article>
    <h1 class="post-title">How to make video 1</h1>
    <p class="post-date">Posted: <time>June 2, 2014</time></p>
    <div class="post-video">
      <div class="screen" role="img" aria-label="Video still of hands measuring a wooden board on a workbench"></div>
      <div class="play">
        <svg width="46" height="46" viewBox="0 0 48 48"><circle cx="24" cy="24" r="21" fill="none" stroke="#fff" stroke-width="4"/><path d="M19 14v20l16-10z" fill="#fff"/></svg>
        PLAY NOW!
      </div>
      <div class="progress"><span style="width:4%"></span></div>
      <div class="controls">
        <svg width="10" height="12" viewBox="0 0 10 12"><rect width="3" height="12" fill="#bbb"/><rect x="6" width="3" height="12" fill="#bbb"/></svg>
        <svg width="14" height="12" viewBox="0 0 14 12"><path d="M0 4h3l4-4v12l-4-4H0z" fill="#bbb"/></svg>
        <span>0:13 / 5:13</span>
      </div>
    </div>
    <p class="post-excerpt">Lorem ipsum dolor sit amet, consectetur adipiscing elit. Fusce lobortis mauris id augue tempus volutpat eget quis dui. Pellentesque quis molestie enim, quis pretium lorem. Ut vitae scelerisque purus. Sed commodo augue a faucibus congue. Ut purus urna, sagittis non neque vel, mollis ullamcorper justo. Etiam quis dui tristique, iaculis turpis et, euismod leo. Mauris vulputate suscipit</p>
    <div class="btn read-more">read more</div>
    <div class="post-rule"></div>
  </article>
  <aside>
    <section class="widget recent">
      <h2 class="widget-title">RECENT VIDEOS</h2>
      <ul class="recent-list">
        <li>
          <div class="thumb" role="img" aria-label="Thumbnail of a woodworking video">
            <div class="play"><svg width="22" height="22" viewBox="0 0 48 48"><circle cx="24" cy="24" r="20" fill="none" stroke="#fff" stroke-width="5"/><path d="M19 14v20l16-10z" fill="#fff"/></svg>PLAY NOW!</div>
            <span class="duration">7:16</span>
          </div>
          <h3>How to make a video 1</h3>
        </li>
        <li>
          <div class="thumb" role="img" aria-label="Thumbnail of a woodworking video">
            <div class="play"><svg width="22" height="22" viewBox="0 0 48 48"><circle cx="24" cy="24" r="20" fill="none" stroke="#fff" stroke-width="5"/><path d="M19 14v20l16-10z" fill="#fff"/></svg>PLAY NOW!</div>
            <span class="duration">5:20</span>
          </div>
          <h3>How to make a video 2</h3>
        </li>
        <li>
          <div class="thumb" role="img" aria-label="Thumbnail of a woodworking video">
            <div class="play"><svg width="22" height="22" viewBox="0 0 48 48"><circle cx="24" cy="24" r="20" fill="none" stroke="#fff" stroke-width="5"/><path d="M19 14v20l16-10z" fill="#fff"/></svg>PLAY NOW!</div>
            <span class="duration">5:08</span>
          </div>
          <h3>How to make a video 3</h3>
        </li>
      </ul>
      <div class="btn see-more">SEE MORE VIDEOS</div>
    </section>
    <div class="hatch"></div>
    <section class="widget archives">
      <h2 class="widget-title">VIDEO ARCHIVES</h2>
    </section>
  </aside>
</main>
</body>
</html>
```